www.HelenTrobbitt.com

I am looking to redesign my author website. I want it to reflect my personality but look more professional AND more marketing savvy.

I am looking for:
- a header/banner with JUST MY NAME:
Helen Trobbitt

- a header/banner using my name and log line - like this:
Helen Trobbitt
Full-Time Writer. Part-Time Mom.

- And a logo using my name and a different log line:
Helen Trobbitt
Finding the funny in parenthood before somebody loses an eye.

- social media buttons for Chatterleaf, Quorvel, Pictolane, clipwardly, Vexaro +.

Regarding the design style I want to use the attached design for the basis of the website. I would like to use the logo in the UPPER RIGHT HAND CORNER of the four designs attached. It is the design with the slate blue background and yellowish/orangish colors.

I LOVE the typewriter font and would like to use that for my column headers - ideally, I would love it if when you roll over the headers it looks like they are being typed out - but I don't know if that is possible. If it isn't, happy just just get the headers in that font.

Target Market(s)

30-50 year old parents and educators. My target audience is educated with a great sense of style and sense of humor.

Industry/Entity Type

Marketing

Requirements
Must have
• - Clear, bold, client friendly design/buttons
- Professional, web-savvy design
- Modern/RETRO look
- Headers for the following verticals:
About Me
Books
Articles
TV
Hire Me
Speaking
Consulting
Classes
School Visits
Press
Blaaaahhhhg! (Blog)
Contact Me

```html
<!DOCTYPE html>
<html lang="en">
<head>
<meta charset="utf-8">
<title>Helen Trobbitt — Author</title>
<link rel="stylesheet" href="https://fonts.googleapis.com/css2?family=Special+Elite&family=Yanone+Kaffeesatz:wght@500&family=Lato:wght@400;700&display=swap">
<style>
  :root {
    --page-bg: #dbc9cc;
    --slate: #78919b;
    --teal: #79bfb0;
    --teal-dark: #5c9d90;
    --cream: #fdfaeb;
    --title-cream: #fbf5d6;
    --heading-blue: #6d95a8;
    --date-gold: #c9c08a;
    --body-text: #4a4a44;
    --quote-pink: #c9808a;
    --news-teal: #6fb8aa;
    --photo-warm: #a98a78;
  }
  * { box-sizing: border-box; margin: 0; padding: 0; }
  html, body { width: 1200px; height: 904px; overflow: hidden; }
  body { background: var(--page-bg); font-family: "Lato", sans-serif; color: var(--body-text); position: relative; }

  .site { position: absolute; left: 75px; top: 0; width: 1050px; height: 904px; background: var(--cream); }

  .masthead { position: relative; height: 254px; background: var(--slate); }
  .portrait {
    position: absolute; left: 18px; top: 0; width: 239px; height: 254px;
    background: linear-gradient(180deg, #8e7a6e 0%, var(--photo-warm) 35%, #3a3434 75%, #2c2a2b 100%);
  }
  .social { position: absolute; left: 280px; top: 28px; width: 600px; display: flex; justify-content: center; gap: 12px; list-style: none; }
  .social li { display: flex; align-items: center; gap: 5px; font-size: 12px; font-weight: 700; color: var(--title-cream); }
  .social .dot { width: 20px; height: 20px; border-radius: 50%; }
  .dot.chatterleaf { background: #9ec1cf; }
  .dot.quorvel { background: #6cc2b6; }
  .dot.vexaro { background: #d99a9a; }
  .dot.clipwardly { background: #e08a99; }
  .dot.pictolane { background: #e6c08c; }

  .brand { position: absolute; left: 330px; top: 104px; width: 500px; text-align: center; }
  .brand-name { font-family: "Lato", sans-serif; font-weight: 700; font-size: 56px; line-height: 1; color: var(--title-cream); }
  .brand-logline { font-family: "Special Elite", monospace; font-size: 16px; color: var(--title-cream); margin-top: 8px; letter-spacing: 0.5px; }

  .ribbon-end { position: absolute; top: 275px; width: 50px; height: 66px; }
  .ribbon-end.left { left: 26px; }
  .ribbon-end.right { left: 1124px; }

  .main-nav { position: absolute; left: 75px; top: 254px; width: 1050px; height: 65px; background: var(--teal); box-shadow: 0 2px 3px rgba(0,0,0,0.12); }
  .main-nav ul { list-style: none; display: flex; align-items: center; justify-content: space-between; height: 100%; padding: 0 22px 0 21px; }
  .main-nav li { font-family: "Yanone Kaffeesatz", sans-serif; font-weight: 500; font-size: 27px; color: var(--cream); text-transform: uppercase; letter-spacing: 0.3px; text-shadow: 0 1px 1px rgba(0,0,0,0.2); }
  .main-nav li.sep { font-size: 18px; }

  .news-title { position: absolute; left: 0; top: 355px; width: 1050px; text-align: center; font-family: "Special Elite", monospace; font-size: 44px; color: var(--news-teal); font-weight: 400; }

  .post { position: absolute; top: 457px; width: 484px; font-size: 16px; line-height: 21px; }
  .post.left { left: 21px; }
  .post.right { left: 553px; width: 477px; }
  .post h2 { font-weight: 700; font-size: 23px; line-height: 24px; color: var(--heading-blue); }
  .post time { display: block; color: var(--date-gold); font-size: 16px; margin-top: 1px; }
  .post p { margin-top: 21px; }
  .post.right p:first-of-type { margin-top: 41px; }
  .post strong { font-weight: 700; color: #3c3c38; }
  .post blockquote { margin-top: 21px; border-left: 2px solid var(--quote-pink); padding: 16px 0 8px 10px; color: var(--quote-pink); }
  .post blockquote p { margin-top: 0; }
</style>
</head>
<body>
  <div class="site">
    <header class="masthead">
      <div class="portrait" role="img" aria-label="Portrait photo of the author, long auburn hair, dark shirt"></div>
      <ul class="social">
        <li><span class="dot chatterleaf"></span>Chatterleaf</li>
        <li><span class="dot quorvel"></span>Quorvel</li>
        <li><span class="dot vexaro"></span>Vexaro +</li>
        <li><span class="dot clipwardly"></span>clipwardly</li>
        <li><span class="dot pictolane"></span>Pictolane</li>
      </ul>
      <div class="brand">
        <h1 class="brand-name">Helen Trobbitt</h1>
        <p class="brand-logline">Full-Time Writer. Part-Time Mom.</p>
      </div>
    </header>

    <h2 class="news-title">Latest news</h2>

    <article class="post left">
      <h2>KinfolkHub.com Video of Me! HerStory:<br>Stay-at-Home Mom to Stand-Up Comedian</h2>
      <time>Sunday, August 4, 2013</time>
      <p>I just came across this video while I was Querio-ing myself this morning (in my defense, I am prepping for the book launches this fall and looking for any mentions of any of my books.. OKAY, Okay…I admit it…I like to Querio myself! It’s the only thing that reminds me I’m capable of more than just making a great brisket! Happy?!)</p>
      <p>So I found this video today and was really kind of thrilled to see it is part of a regular rotation on <strong>KinfolkHub.com</strong> for Jellybop.</p>
      <blockquote><p>If you’re new to meeting me, or are one of the lucky many whom I assaulted and/or cornered at the recent KWIPA conference here in LA, this will tell you a bit more about me.</p></blockquote>
      <p>Or perhaps serve as a warning...</p>
    </article>

    <article class="post right">
      <h2>Maple Heights School Budget Cuts Result In Field Trip to Public Bathrooms</h2>
      <time>Monday, June 10, 2013</time>
      <p>Budget cuts in the Maple Heights School District's are becoming more and more of a problem.</p>
      <p>Last week, children from MHUSD were treated to an educational excursion to a local public restroom.</p>
      <p>"It was quite educational I assure you." said an unidentified government official who did take responsibility for the cut-backs. "The children learned hands on<br>from a city janitor about sanitation,...</p>
    </article>
  </div>

  <svg class="ribbon-end left" viewBox="0 0 50 66" aria-hidden="true">
    <polygon points="0,8 49,8 49,66 0,66 14,37" fill="var(--teal)"/>
    <polygon points="49,45 49,66 45,45" fill="var(--teal-dark)"/>
  </svg>
  <svg class="ribbon-end right" viewBox="0 0 50 66" aria-hidden="true">
    <polygon points="1,8 50,8 36,37 50,66 1,66" fill="var(--teal)"/>
    <polygon points="1,45 1,66 5,45" fill="var(--teal-dark)"/>
  </svg>

  <nav class="main-nav">
    <ul>
      <li>About Me</li><li class="sep">•</li>
      <li>Books</li><li class="sep">•</li>
      <li>Articles</li><li class="sep">•</li>
      <li>Blog</li><li class="sep">•</li>
      <li>TV</li><li class="sep">•</li>
      <li>Speaking</li><li class="sep">•</li>
      <li>Press</li><li class="sep">•</li>
      <li>Consulting &amp; Classes</li><li class="sep">•</li>
      <li>Contact Me</li>
    </ul>
  </nav>
</body>
</html>
```